Long Established Local Fencing (not swords) Business needs fresh Business Cards

We need fresh double sided business cards for our Fencing Construction business, we are looking for something with our new logo design added, and maybe a photo background ?
We recently had cards made from Cardlyne and we were horrified with what we got back, the quality was terrible, so am looking for high quality format for good printing company to make.
We install Steelmora, Timber paling, Aluminium Slat Screening, Picket (timber and aluminium) and most other fencing installations.
Our website is brankelrails.com.au should you like to learn a bit more.
We do have logo in other formats if required.
We have been in business for over 35 years and we have used this as a "motto" it is on our signage

Industry/Entity Type

Construction

Contact Information for Business Card

Open to ideas, we need 3 x different cards, one generic with no name and 2 x others each with 1 of our bosses name on each, I will put into upload files.

Colors
ec1f27
000000
606060
f5f5f5

Requirements
Must have
• Company Name and Logo
• Address
• Contact details, phone, website, email etc
• Small space to write notes when leaving card at residence
Nice to have
• Our motto "Servicing the Peninsula for over 35 years"

```html
<!DOCTYPE html>
<html lang="en">
<head>
<meta charset="utf-8">
<title>Brankel Rails — Business Card</title>
<link rel="stylesheet" href="https://fonts.googleapis.com/css2?family=Saira:wght@400;500;700;800&display=swap">
<style>
  :root {
    --brand-red: #dc3232;
    --brand-black: #131416;
    --brand-grey: #606060;
    --card-white: #f5f5f5;
    --stage: #8c8c8c;
    --text-dark: #1d1d1d;
  }
  * { margin: 0; padding: 0; box-sizing: border-box; }
  html, body { width: 1200px; height: 1200px; overflow: hidden; }
  body {
    position: relative;
    background: var(--stage);
    font-family: "Saira", Arial, sans-serif;
  }
  .card {
    position: absolute;
    top: 310px;
    width: 364px;
    height: 594px;
    border-radius: 16px;
    overflow: hidden;
    box-shadow: 3px 4px 6px rgba(0,0,0,.35);
  }
  .card--front { left: 234px; background: var(--card-white); }
  .card--back { left: 628px; background: var(--brand-black); }

  .brand {
    position: absolute;
    left: 0; right: 0; top: 106px;
    text-align: center;
  }
  .brand__mark {
    display: block;
    width: 64px; height: 64px;
    margin: 0 auto 40px;
    border-radius: 50%;
    background: var(--brand-red);
  }
  .brand__name {
    font-weight: 800;
    font-size: 42px;
    line-height: 44px;
    letter-spacing: 2px;
    color: var(--brand-black);
  }

  .person {
    position: absolute;
    left: 0; right: 0; top: 396px;
    text-align: center;
  }
  .person__name {
    font-weight: 700;
    font-size: 20px;
    color: var(--brand-red);
    line-height: 24px;
  }
  .person__role {
    font-size: 16px;
    color: var(--text-dark);
    line-height: 20px;
  }

  .contact-divider {
    position: absolute;
    left: 89px; top: 460px;
    width: 187px; height: 20px;
    display: flex; align-items: center; justify-content: center; gap: 3px;
  }
  .contact-divider::before, .contact-divider::after {
    content: ""; flex: 1; height: 1px; background: #9a9a9a;
  }
  .contact-divider::before { margin-right: 5px; }
  .contact-divider::after { margin-left: 5px; }
  .contact-divider svg { width: 19px; height: 19px; }

  .contact {
    position: absolute;
    left: 0; right: 0; top: 487px;
    text-align: center;
    list-style: none;
    font-size: 16px;
    line-height: 22px;
    color: var(--text-dark);
  }

  .back__field { position: absolute; inset: 0; width: 100%; height: 100%; }
  .motto {
    position: absolute;
    left: 0; right: 0; top: 505px;
    text-align: center;
    font-size: 18px;
    line-height: 29px;
    color: var(--card-white);
    letter-spacing: .3px;
  }
</style>
</head>
<body>
  <section class="card card--front">
    <div class="brand">
      <span class="brand__mark"></span>
      <div class="brand__name">BRANKEL<br>RAILS</div>
    </div>
    <div class="person">
      <div class="person__name">DANIEL HARLOW</div>
      <div class="person__role">Managing Director</div>
    </div>
    <div class="contact-divider">
      <svg viewBox="0 0 20 20" aria-label="phone"><circle cx="10" cy="10" r="10" fill="var(--brand-red)"/><path d="M7 5.5l1.6 2.3-1 1.2c.7 1.4 1.7 2.4 3 3l1.2-1 2.3 1.6-.9 1.6c-3.8-.5-6.6-3.3-7.1-7.1z" fill="#fff"/></svg>
      <svg viewBox="0 0 20 20" aria-label="email"><circle cx="10" cy="10" r="10" fill="var(--brand-red)"/><rect x="5" y="6.5" width="10" height="7" fill="#fff"/><path d="M5 6.5l5 4 5-4" stroke="var(--brand-red)" fill="none"/></svg>
      <svg viewBox="0 0 20 20" aria-label="website"><circle cx="10" cy="10" r="10" fill="var(--brand-red)"/><circle cx="10" cy="10" r="5" fill="none" stroke="#fff" stroke-width="1.4"/><path d="M5 10h10M10 5v10" stroke="#fff" stroke-width="1.2"/></svg>
    </div>
    <ul class="contact">
      <li>444 555 6688</li>
      <li>info@youremail.com</li>
      <li>www.websitename.com</li>
    </ul>
  </section>

  <section class="card card--back">
    <svg class="back__field" viewBox="0 0 364 594" preserveAspectRatio="none" aria-hidden="true">
      <path d="M0 320 C 40 380, 150 375, 250 320 C 320 280, 364 240, 364 200 L364 594 L0 594 Z" fill="var(--brand-red)"/>
    </svg>
    <p class="motto">SERVICING THE PENINSULA<br>FOR OVER 35 YEARS</p>
  </section>
</body>
</html>
```